Business to Business Website Homepage Design

Hi, My Web Developer is giving me designs that aren't quite taking my fancy as far as visual impact. I'd love to see designs come out which are simple, fresh and powerful.
I just want a PDF document that I can give to my web developer to follow, so this project is NOT to make a website, its to design the homepage.
I would like it to scroll down through different areas of my website on the homepage. Our colours are Blood Orange, White, Grey & Black.
I like these websites:
Simplicity
https://www.quenvalo.com/au/webapps/mpp/home
Our Team Section
http://trelmicode.com.au/
We'd like our logo on top left. Nav bar top right. Have an image which we can place a headline subject on + video icon which will pop out with a video and opt in for name and email with a heading so people know what they're opting in for.
The next section should have a lot of white space, this "What we do" which is 1) Grow in size so your business can get bigger 2) increase in value, so you maximise what your business is worth 3) Free up your time, so you can live the lifestyle you've always wanted. Our brief was we want image/text combo with a lot of white space,
Then we have our services
After Services, would like to have a "Why Work With Us" section
Then a testimonials section
Then "Our Team"
Then contact us.
Thats pretty much it, we'd just love some different ideas, these guys are almost there, but just need more impact.
Updates
Target Market(s)
Business Owners between $1m to $3m turnover
Industry/Entity Type
Business
Number of Pages Required
1 page
Look and feel
Each slider illustrates characteristics of the customer's brand and the style your logo design should communicate.

```html
<!DOCTYPE html>
<html lang="en">
<head>
<meta charset="utf-8">
<title>Kestrel Partners – Home</title>
<link href="https://fonts.googleapis.com/css2?family=Raleway:wght@400;500;600;700&display=swap" rel="stylesheet">
<style>
:root{
  --red:#c5302a;
  --pink:#ebbab6;
  --black:#0d0d0d;
  --ink:#3a3a3a;
  --muted:#777;
  --grey-bg:#f4f4f4;
  --line:#e3e3e3;
  --white:#fff;
}
*{margin:0;padding:0;box-sizing:border-box}
html,body{width:680px;height:1200px;overflow:hidden;background:var(--white)}
body{position:relative;font-family:"Raleway",sans-serif;color:var(--ink)}
.abs{position:absolute}
/* hero */
.hero{left:0;top:0;width:680px;height:434px;background:linear-gradient(120deg,#6d6d6d 0%,#4a4a4a 35%,#2b2d33 70%,#3d3f45 100%)}
.hero-shade{left:0;top:0;width:680px;height:434px;background:rgba(0,0,0,.25)}
.site-header{left:48px;top:0;width:584px;height:64px;background:var(--white);display:flex;align-items:center;justify-content:space-between;padding:0 6px 0 10px}
.brand{color:var(--ink);font-weight:600;font-size:13px;letter-spacing:.5px;line-height:1}
.main-nav{display:flex;font-size:10px;color:#666;margin-top:2px}
.main-nav a{color:inherit;text-decoration:none;padding:0 6px;border-left:1px solid #ddd;line-height:12px}
.main-nav a:first-child{border-left:none}
.main-nav a.is-active{color:var(--ink);border-bottom:2px solid var(--red);padding-bottom:3px}
.hero-title{left:0;width:680px;top:112px;text-align:center;color:var(--white);font-size:26px;font-weight:500;line-height:36px}
.hero-title .sep{color:var(--red)}
.rule{height:3px;background:var(--red)}
.hero-rule{left:304px;top:189px;width:72px}
.hero-lead{left:0;width:680px;top:217px;text-align:center;color:#eee;font-size:14.5px;line-height:21px}
.btn-signup{left:291px;top:277px;width:98px;height:26px;background:var(--red);color:var(--white);font-size:11px;font-weight:600;display:flex;align-items:center;justify-content:center;border-radius:2px}
.play{left:328px;top:322px}
/* features */
.features{left:48px;top:374px;width:584px;height:134px;display:flex;background:var(--white);box-shadow:0 1px 0 var(--line)}
.feature{flex:1;text-align:center;padding-top:12px;border-left:1px solid var(--line)}
.feature:first-child{border-left:none;background:var(--pink)}
.feature h3{font-size:10px;font-weight:500;line-height:12.5px;margin:14px 20px 0;color:var(--ink)}
.feature p{font-size:7px;line-height:10.5px;color:var(--muted);margin:12px 30px 0}
/* headings */
.section-title{left:0;width:680px;text-align:center;color:var(--red);font-size:13px;font-weight:500}
/* services */
.service{width:126px}
.service h4{font-size:12px;font-weight:500;color:var(--ink);margin-bottom:4px;letter-spacing:.2px;white-space:nowrap}
.service p{font-size:7px;line-height:10.5px;color:#555}
.service p span{color:var(--red)}
/* team */
.team{left:0;top:780px;width:680px;height:216px;background:var(--grey-bg)}
.member{width:100px;text-align:center}
.avatar{width:56px;height:56px;margin:0 auto;border-radius:50%;border:3px solid var(--white);box-shadow:0 0 0 1px #ddd;background:radial-gradient(circle at 50% 40%,#d9b8a2,#8a7060)}
.member h5{font-size:8.5px;font-weight:500;margin-top:10px;color:#555}
.member small{display:block;font-size:6.5px;color:var(--muted);margin-top:4px}
.member.is-active h5,.member.is-active small{color:var(--red)}
.member.is-active .avatar{background:radial-gradient(circle at 50% 40%,#d88a70,#b2402e)}
/* bottom */
.quote-title,.contact-title{font-size:13px;font-weight:600;color:var(--white)}
.quote-text{left:194px;top:1062px;width:170px;color:var(--white);font-size:9.5px;line-height:13px}
.client-photo{left:94px;top:1059px;width:58px;height:58px;border-radius:50%;border:2px solid var(--white);background:radial-gradient(circle at 50% 40%,#b57f63,#5a3a2a)}
.contact-list{left:454px;top:1060px;color:var(--white);font-size:9px;line-height:13px;list-style:none}
.contact-list li{display:flex;gap:5px;margin-bottom:14px}
.contact-list svg{flex:none;margin-top:2px}
.copyright{left:48px;top:1180px;color:#f3d4d1;font-size:7.5px}
.social{left:474px;top:1182px;display:flex;gap:12px}
.social span{width:8px;height:8px;border-radius:50%;background:var(--white)}
</style>
</head>
<body>

<div class="abs hero" role="img" aria-label="Photo of business people in suits working at a laptop"></div>
<div class="abs hero-shade"></div>

<header class="abs site-header">
  <div class="brand">KESTREL PARTNERS</div>
  <nav class="main-nav">
    <a class="is-active" href="#">HOME</a><a href="#">ABOUT US</a><a href="#">OUR SERVICES</a><a href="#">OUR TEAM</a><a href="#">CONTACT US</a>
  </nav>
</header>

<h1 class="abs hero-title">YOUR BUSINESS <span class="sep">•</span> YOUR SUCCESS<br>YOUR LIFESTYLE</h1>
<div class="abs rule hero-rule"></div>
<p class="abs hero-lead">Consectetur adipisicing elit, sed do eiusmod tempor<br>incididunt ut labore et dolore magna aliqua.</p>
<div class="abs btn-signup">SIGN UP NOW</div>
<svg class="abs play" width="24" height="24" viewBox="0 0 24 24" aria-label="Play video"><circle cx="12" cy="12" r="10.5" fill="none" stroke="#fff" stroke-width="1.5"/><path d="M9.5 7.5v9l7-4.5z" fill="#fff"/></svg>

<section class="abs features">
  <div class="feature">
    <svg width="28" height="28" viewBox="0 0 28 28"><path d="M2 2v24h24" fill="none" stroke="#c5302a" stroke-width="1.5"/><rect x="7" y="16" width="3" height="8" fill="#c5302a"/><rect x="12" y="13" width="3" height="11" fill="#c5302a"/><rect x="17" y="10" width="3" height="14" fill="#c5302a"/><rect x="22" y="7" width="3" height="17" fill="#c5302a"/><path d="M5 14l8-7 5 3 7-7" fill="none" stroke="#c5302a" stroke-width="1.5"/></svg>
    <h3>Grow in size so your business<br>can get bigger</h3>
    <p>Sed do eiusmod tempor incididunt ut labore et dolore magna aliqua. Ut enim ad minim veniam quis.</p>
  </div>
  <div class="feature">
    <svg width="30" height="28" viewBox="0 0 30 28"><rect x="2" y="3" width="20" height="22" rx="2" fill="#c5302a"/><g fill="#fff"><rect x="5" y="7" width="14" height="3"/><rect x="5" y="13" width="3" height="3"/><rect x="10" y="13" width="3" height="3"/><rect x="5" y="18" width="3" height="3"/><rect x="10" y="18" width="3" height="3"/></g><circle cx="22" cy="19" r="7" fill="#c5302a" stroke="#fff" stroke-width="1.5"/><path d="M19 19l2.5 2.5 4-4" fill="none" stroke="#fff" stroke-width="1.5"/></svg>
    <h3>Free up your time, so you can<br>live the lifestyle</h3>
    <p>Ut enim ad minim veniam quis. nostrud exercitation ullamco laboris nisi ut aliquip ex ea commodo.</p>
  </div>
  <div class="feature">
    <svg width="28" height="28" viewBox="0 0 28 28"><g fill="#c5302a"><rect x="3" y="18" width="3" height="8"/><rect x="8" y="15" width="3" height="11"/><rect x="13" y="12" width="3" height="14"/><rect x="18" y="9" width="3" height="17"/><rect x="23" y="6" width="3" height="20"/><path d="M3 14l14-9-2-2h9v9l-2-2-18 9z"/></g></svg>
    <h3>Free up your time, so you can<br>live the lifestyle</h3>
    <p>Ut enim ad minim veniam quis. nostrud exercitation ullamco laboris nisi ut aliquip ex ea commodo.</p>
  </div>
</section>

<h2 class="abs section-title" style="top:547px">OUR SERVICES</h2>
<div class="abs rule" style="left:318px;top:568px;width:44px;height:2px"></div>

<svg class="abs" style="left:60px;top:600px" width="28" height="14" viewBox="0 0 28 14"><g fill="#c5302a"><circle cx="5" cy="4" r="3"/><circle cx="14" cy="4" r="3"/><circle cx="23" cy="4" r="3"/><path d="M0 13a5 5 0 0 1 10 0zM9 13a5 5 0 0 1 10 0zM18 13a5 5 0 0 1 10 0z"/></g></svg>
<div class="abs service" style="left:99px;top:599px;width:112px"><h4>PEOPLE</h4><p>Incididunt ut labore et dolore magna aliqua. Ut enim ad minim veniam, quis nostrud. Exercitation ullamco. <span>READ MORE</span></p></div>

<svg class="abs" style="left:250px;top:599px" width="26" height="16" viewBox="0 0 26 16"><g fill="none" stroke="#c5302a" stroke-width="2"><path d="M2 8l6-6 6 6-6 6z"/><path d="M10 8l6-6 6 6-6 6z"/><path d="M18 4l4 4-4 4"/></g></svg>
<div class="abs service" style="left:286px;top:599px"><h4>NEW EARNING STREAMS</h4><p>Exercitation ullamco laboris nisi ut aliquip ex ea commodo consequat. Duis aute irure dolor in reprehenderit in voluptate velit. <span>READ MORE</span></p></div>

<svg class="abs" style="left:460px;top:599px" width="24" height="16" viewBox="0 0 24 16"><path d="M1 4l5-3 6 3 6-3 5 3-4 8-3 2-4-3-3 2-5-4z" fill="#c5302a"/></svg>
<div class="abs service" style="left:497px;top:599px"><h4>NEW BUSINESSES</h4><p>Duis aute irure dolor in reprehenderit in voluptate velitesse cillum dolore eu fugiat nulla pariatur. Excepteur sint occaecat. <span>READ MORE</span></p></div>

<svg class="abs" style="left:72px;top:690px" width="16" height="18" viewBox="0 0 16 18"><path d="M5 1h6l-2 4a7 7 0 1 1-2 0z" fill="#c5302a"/><text x="8" y="14.5" font-size="8" fill="#fff" text-anchor="middle" font-family="Raleway,sans-serif" font-weight="700">$</text></svg>
<div class="abs service" style="left:99px;top:692px;width:112px"><h4>FUNDING</h4><p>Laboris nisi ut aliquip ex ea commodo consequat. Duis aute irure dolor in reprehenderit in voluptate velit. <span>READ MORE</span></p></div>

<svg class="abs" style="left:255px;top:692px" width="20" height="16" viewBox="0 0 20 16"><g fill="#c5302a"><circle cx="12" cy="3" r="3"/><path d="M6 16a6 6 0 0 1 12 0z"/><rect x="1" y="7" width="9" height="8" rx="1"/></g></svg>
<div class="abs service" style="left:286px;top:692px"><h4>NEW MARKETS</h4><p>Esse cillum dolore eu fugiat nulla pariatur. Excepteur sint occaecat cupidatat non proident, sunt in culpa qui officia. <span>READ MORE</span></p></div>

<svg class="abs" style="left:467px;top:692px" width="18" height="15" viewBox="0 0 18 15"><g fill="#c5302a"><path d="M6 1h6v3h-1.5V2.5h-3V4H6z"/><rect x="0" y="4" width="18" height="11" rx="1.5"/></g><rect x="0" y="8" width="18" height="1.2" fill="#fff"/></svg>
<div class="abs service" style="left:497px;top:692px"><h4>BUSINESS SYSTEMS</h4><p>Cillum dolore eu fugiat nulla pariatur. Excepteur sint occaecatupidatat non proident, sunt in culpa qui officia deserunt mollit. <span>READ MORE</span></p></div>

<section class="abs team"></section>
<h2 class="abs section-title" style="top:805px">OUR TEAM</h2>
<div class="abs rule" style="left:318px;top:826px;width:44px;height:2px"></div>
<svg class="abs" style="left:46px;top:858px" width="22" height="42" viewBox="0 0 22 42"><path d="M20 2L2 21l18 19" fill="none" stroke="#ccc" stroke-width="1.2"/></svg>
<svg class="abs" style="left:610px;top:858px" width="22" height="42" viewBox="0 0 22 42"><path d="M2 2l18 19L2 40" fill="none" stroke="#ccc" stroke-width="1.2"/></svg>
<div class="abs member" style="left:124px;top:855px"><div class="avatar" role="img" aria-label="Portrait of Tom Reilly"></div><h5>TOM REILLY</h5><small>Business Manager</small></div>
<div class="abs member is-active" style="left:235px;top:855px"><div class="avatar" role="img" aria-label="Portrait of Mia Santos"></div><h5>MIA SANTOS</h5><small>Accounts Manager</small></div>
<div class="abs member" style="left:346px;top:855px"><div class="avatar" role="img" aria-label="Portrait of Leo Harmon"></div><h5>LEO HARMON</h5><small>Marketing Expert</small></div>
<div class="abs member" style="left:456px;top:855px"><div class="avatar" role="img" aria-label="Portrait of Kate Orwell"></div><h5>KATE ORWELL</h5><small>Accounts Manager</small></div>

<svg class="abs" style="left:0;top:996px" width="680" height="204" viewBox="0 0 680 204">
  <rect x="0" y="9" width="680" height="195" fill="#0d0d0d"/>
  <polygon points="0,0 370,0 462,204 0,204" fill="#c5302a"/>
  <line x1="0" y1="176" x2="680" y2="176" stroke="rgba(255,255,255,.35)" stroke-width="0.8"/>
</svg>

<h2 class="abs quote-title" style="left:48px;top:1020px">WHAT OUR CUSTOMERS SAY</h2>
<div class="abs rule" style="left:48px;top:1043px;width:44px;height:2px;background:#fff"></div>
<div class="abs client-photo" role="img" aria-label="Portrait of a satisfied customer"></div>
<span class="abs" style="left:167px;top:1050px;color:#fff;font-size:18px;font-weight:700">“</span>
<p class="abs quote-text">Enim ad minim veniam, quis nostrud exercitation ullamco laboris nisi ut aliquip ex ea commodo consequat. Duis aute irure dolor. &nbsp;&nbsp;<b>“</b></p>
<svg class="abs" style="left:164px;top:1138px" width="54" height="8" viewBox="0 0 54 8"><circle cx="4" cy="4" r="2.6" fill="#e08a84"/><circle cx="19" cy="4" r="2.6" fill="#e08a84"/><circle cx="34" cy="4" r="2.6" fill="#fff"/><circle cx="49" cy="4" r="2.6" fill="#e08a84"/></svg>

<h2 class="abs contact-title" style="left:454px;top:1020px">CONTACT US</h2>
<div class="abs rule" style="left:454px;top:1043px;width:44px;height:2px;background:#fff"></div>
<ul class="abs contact-list">
  <li><svg width="9" height="11" viewBox="0 0 9 11"><path d="M4.5 10.5S1 6.5 1 4.3a3.5 3.5 0 0 1 7 0c0 2.2-3.5 6.2-3.5 6.2z" fill="none" stroke="#fff"/><circle cx="4.5" cy="4.3" r="1.2" fill="#fff"/></svg><span>52 Larkin Lane, Brenmore, SA,<br>5900, Australia</span></li>
  <li><svg width="10" height="10" viewBox="0 0 10 10"><circle cx="5" cy="5" r="4.4" fill="none" stroke="#fff"/><path d="M3.5 2.8l1 1-.6.8a4 4 0 0 0 1.5 1.5l.8-.6 1 1-.8.8c-1.8-.3-3.4-1.9-3.7-3.7z" fill="#fff"/></svg><span>08 5550 1374</span></li>
  <li><svg width="10" height="8" viewBox="0 0 10 8"><rect width="10" height="8" fill="#fff"/><path d="M0 0l5 4 5-4" fill="none" stroke="#0d0d0d"/></svg><span>info@kestrelpartners.com</span></li>
</ul>

<p class="abs copyright">©Kestrelpartners2015 All Rights Reserved</p>
<div class="abs social" aria-label="Social links"><span></span><span></span><span></span></div>

</body>
</html>
```